Dental Practice Billboard Design

We are a newer dental practice in need of a simple but appealing billboard for our growing dental practice to attract new patients. The practice is owned by husband and wife dentists and is family friendly in a small town in Kentucky. We try to be very friendly and caring to our patients. Would prefer a blue background for the billboard and our tooth logo to be prominent. We are partial to the Patua One font used in the image below but please feel free to tweak it as you deem necessary. The shape of the uppercase D and lowercase g are why we like that font, so fonts with a similarly shaped “D” and “g” would work as well. Please include our phone number (606) 847-3962. Please see our website Harlowfamilydentistry.com for more info on the practice if needed. Thank you! Looking forward to seeing your creation.
Updates

The dimensions will be 12ft x 24ft (3.6576m x 7.3152m). Apologies for not including this in the original prompt. Thank you all for your submissions.

Industry/Entity Type

Dental

Font styles to use
Other font styles liked:
• Patua One

Colors
0054AA
0677BA
7BADD7
CADEEF
E8F1F8
0094D4
00A9DD
6FCCEA
C7EBF8
E9F6FB
00AB8E
00BBA5
67D7C9
C6EFE9
E9F9F6
59FF00
82FF00
B8FF75
E3FFCB
F4FFEA

Requirements
Must have
• Phone number, website, Logo, Practice name “Harlow Family Dentistry”
Should not have
• A tagline or slogan

```html
<!DOCTYPE html>
<html lang="en">
<head>
<meta charset="utf-8">
<title>Harlow Family Dentistry – Billboard</title>
<link rel="stylesheet" href="https://fonts.googleapis.com/css2?family=Patua+One&family=Fira+Sans:wght@500&display=swap">
<style>
  :root {
    --page-bg: #eef1f5;
    --board-blue: #2a48a8;
    --band-white: #f4f5f2;
    --text-white: #f6f6f2;
    --accent-green: #2fa83a;
  }
  * { margin: 0; padding: 0; box-sizing: border-box; }
  html, body {
    width: 1200px;
    height: 900px;
    overflow: hidden;
    background: var(--page-bg);
  }
  .billboard {
    position: absolute;
    left: 40px;
    top: 170px;
    width: 1120px;
    height: 560px;
    background: var(--board-blue);
    overflow: hidden;
    box-shadow: 0 10px 30px rgba(20, 30, 70, 0.18);
  }
  .brand-mark {
    position: absolute;
    left: 50px;
    top: 190px;
    width: 230px;
    display: flex;
    flex-direction: column;
    align-items: center;
    gap: 18px;
  }
  .brand-mark__dot {
    width: 70px;
    height: 70px;
    border-radius: 50%;
    background: var(--accent-green);
  }
  .brand-mark__name {
    font-family: "Patua One", serif;
    font-size: 52px;
    color: var(--text-white);
    line-height: 1;
  }
  .practice-name {
    position: absolute;
    left: 330px;
    right: 30px;
    top: 138px;
    font-family: "Patua One", serif;
    font-weight: 400;
    font-size: 66px;
    line-height: 1;
    color: var(--text-white);
    white-space: nowrap;
  }
  .web-band {
    position: absolute;
    left: 320px;
    top: 250px;
    right: 0;
    height: 86px;
    background: var(--band-white);
    border-radius: 43px 0 0 43px;
    display: flex;
    align-items: center;
    padding-left: 36px;
  }
  .website {
    font-family: "Patua One", serif;
    font-size: 40px;
    letter-spacing: 1px;
    color: var(--accent-green);
    white-space: nowrap;
  }
  .phone {
    position: absolute;
    left: 440px;
    top: 368px;
    font-family: "Fira Sans", sans-serif;
    font-weight: 500;
    font-size: 92px;
    line-height: 1;
    letter-spacing: 2px;
    color: var(--text-white);
    white-space: nowrap;
  }
</style>
</head>
<body>
  <main class="billboard">
    <div class="brand-mark">
      <span class="brand-mark__dot"></span>
      <span class="brand-mark__name">Harlow</span>
    </div>
    <h1 class="practice-name">Harlow Family Dentistry</h1>
    <div class="web-band">
      <p class="website">Harlowfamilydentistry.com</p>
    </div>
    <p class="phone">(606) 847-3962</p>
  </main>
</body>
</html>
```